Design a single page Shopify store web page

We are looking to have a page designed for a single page Shopify store with 2 products. We already have a basic structure that we like, though we are open to suggestions. We are looking for somebody to provide a design/color scheme that we can then implement using Shopify's templating system. We can handle the implementation(HTML / CSS / jS) as we already have 2 web developers on the team, but have not been able to find a design we liked.

The job would consist of providing a mockup (photoshop or otherwise) and any vector graphics you choose to create for the site (we can provide product photos and other images).

You can also look at http://tidewrenco.com.au for some of our design direction we have used so far

Target Market(s)

Young Australian Males (18 - 49)

Industry/Entity Type

Store

Number of Pages Required

1 page

Font styles to use
Serif
Sans Serif

Requirements
Must have
• Single Page Design
• E-commerce Product Purchase
• Manly (whatever interpretation of that you have)

```html
<!DOCTYPE html>
<html lang="en">
<head>
<meta charset="utf-8">
<title>Tidewren Co — Underwear and Socks Delivered</title>
<link rel="stylesheet" href="https://fonts.googleapis.com/css2?family=Fira+Sans+Condensed:wght@400;600;700&display=swap">
<style>
:root{
  --red:#dc1f3c;
  --red-dark:#b9182f;
  --ink:#23252e;
  --ink-soft:#2c2f3a;
  --navy:#1f2330;
  --panel:#262a36;
  --plan-bg:#e8ecf3;
  --plan-card:#cfd4de;
  --white:#ffffff;
  --text:#3a3a3a;
  --muted:#c8ccd6;
  --font:"Fira Sans Condensed", "Arial Narrow", sans-serif;
}
*{box-sizing:border-box;margin:0;padding:0}
html,body{width:720px;height:1200px;overflow:hidden;background:var(--white)}
body{font-family:var(--font);color:var(--text);position:relative}
.canvas{position:relative;width:720px;height:1200px;overflow:hidden;background:var(--white)}
.abs{position:absolute}

/* Hero */
.hero{left:84px;top:0;width:552px;height:295px;overflow:hidden}
.hero-photo{position:absolute;inset:0;background:
  radial-gradient(ellipse at 70% 40%, rgba(140,50,60,.55), transparent 45%),
  radial-gradient(ellipse at 30% 35%, rgba(190,190,200,.35), transparent 40%),
  linear-gradient(180deg,#4a5266 0%,#3a4154 45%,#2f3444 100%)}
.topbar{position:absolute;left:0;top:0;width:552px;height:31px;background:rgba(30,33,44,.85)}
.logo{position:absolute;left:70px;top:4px;font-size:19px;font-weight:700;color:var(--red);letter-spacing:.2px}
.nav{position:absolute;left:226px;top:0;display:flex;height:31px;align-items:center}
.nav a{color:var(--white);font-size:8px;text-decoration:none;padding:0 10px;height:21px;line-height:21px;text-transform:uppercase;letter-spacing:.3px}
.nav a.is-active{background:var(--red)}
.signup{position:absolute;left:434px;top:6px;width:48px;height:18px;background:var(--red);color:var(--white);font-size:8px;font-weight:700;text-align:center;line-height:18px;text-transform:uppercase}
.hero-title{position:absolute;left:0;top:160px;width:552px;text-align:center;color:var(--white);font-size:17px;font-weight:700;line-height:20px}
.hero-title em{font-style:normal;color:var(--red)}
.signup-panel{position:absolute;left:70px;top:245px;width:412px;height:50px;background:rgba(28,30,40,.92)}
.signup-panel .hint{position:absolute;top:6px;font-size:6.5px;color:var(--red)}
.email-field{position:absolute;left:9px;top:19px;width:193px;height:21px;background:var(--white);color:var(--ink);font-size:8px;text-align:center;line-height:21px}
.notify-btn{position:absolute;left:211px;top:19px;width:193px;height:21px;background:var(--red);color:var(--white);font-size:8px;text-align:center;line-height:21px}

/* How it works */
.section-title{position:absolute;width:720px;left:0;text-align:center;font-weight:700;text-transform:uppercase;color:var(--ink)}
.steps-title{top:318px;font-size:11px}
.step{position:absolute;top:350px;width:134px;height:64px;background:var(--red);color:var(--white)}
.step svg.icon{position:absolute;left:7px;top:13px}
.step h3{position:absolute;left:42px;top:13px;font-size:7px;font-weight:700;text-transform:uppercase}
.step p{position:absolute;left:42px;top:22px;width:86px;font-size:6.3px;line-height:7.4px}
.step-num{position:absolute;left:56px;top:54px;width:22px;height:22px;border-radius:50%;background:var(--white);border:2px solid var(--red);color:var(--ink);font-size:9px;font-weight:700;text-align:center;line-height:18px}

/* Plans */
.plans{left:84px;top:458px;width:552px;height:257px;background:var(--plan-bg)}
.plans-title{top:472px;font-size:15px}
.plan-card{position:absolute;top:502px;width:204px;height:141px;background:var(--plan-card);border-top:4px solid var(--ink)}
.plan-tab{position:absolute;top:-4px;width:40px;height:18px;background:var(--ink);color:var(--white);font-size:7px;font-weight:600;line-height:18px;text-align:center}
.photo{position:absolute}
.price{position:absolute;top:121px;height:14px;width:37px;background:var(--ink);color:var(--white);font-size:7px;text-align:center;line-height:14px}
.buy{position:absolute;top:121px;height:14px;width:36px;background:var(--red);color:var(--white);font-size:7px;text-align:center;line-height:14px}
.perks{position:absolute;left:152px;top:660px;width:414px;height:38px;background:var(--red)}
.perk{position:absolute;top:6px;width:92px;height:26px}
.perk svg{position:absolute;left:0;top:0}
.perk span{position:absolute;left:24px;top:0;line-height:26px;font-size:5.8px;font-weight:600;color:var(--white);white-space:nowrap}

/* FAQ */
.faq{left:84px;top:715px;width:552px;height:297px;background:linear-gradient(180deg,#353b4d 0%,#2a2f3e 55%,#232734 100%)}
.faq-title{top:731px;font-size:14px;color:var(--red)}
.faq-card{position:absolute;width:133px;height:103px;background:rgba(24,26,34,.82);color:var(--white);text-align:center;padding:8px 7px}
.faq-card h3{font-size:8px;font-weight:700;color:var(--red);line-height:10px;min-height:20px}
.faq-card p{font-size:5.8px;line-height:7.6px;color:var(--muted);margin-top:6px}
.dot{position:absolute;top:989px;width:10px;height:10px;border-radius:2px;background:#444a5a}
.dot.is-active{background:var(--red);border-radius:50%}

/* About */
.about{left:84px;top:1012px;width:552px;height:150px;background:var(--red);color:var(--white);text-align:center}
.about h2{position:absolute;width:552px;top:17px;font-size:14px;color:var(--ink);text-transform:uppercase}
.about h3{position:absolute;width:552px;top:44px;font-size:11px;font-weight:700}
.about h3 em{font-style:normal;color:var(--ink)}
.about .lead{position:absolute;width:552px;top:60px;font-size:8.5px}
.about .body{position:absolute;left:60px;top:82px;width:432px;font-size:6px;line-height:9px}

/* Footer */
.footer{left:84px;top:1162px;width:552px;height:38px;background:var(--ink)}
.footer .copy{position:absolute;left:70px;top:15px;font-size:5.5px;color:var(--red)}
.footer .connect{position:absolute;left:424px;top:4px;font-size:5.5px;color:var(--red)}
.social{position:absolute;top:14px;width:14px;height:14px;background:var(--red);border-radius:2px}
</style>
</head>
<body>
<div class="canvas">

  <header class="abs hero">
    <div class="hero-photo" role="img" aria-label="Photo of two young men in open shirts modelling underwear against a tiled wall"></div>
    <div class="topbar">
      <div class="logo">Tidewren Co</div>
      <nav class="nav">
        <a class="is-active" href="#how">How it works</a>
        <a href="#plans">Plans</a>
        <a href="#faq">FAQ</a>
        <a href="#about">About us</a>
      </nav>
      <div class="signup">Signup</div>
    </div>
    <h1 class="hero-title">New <em>Underwear</em> and <em>Socks</em> Delivered to<br>Your Door Every <em>3</em> or <em>6</em> Month</h1>
    <div class="signup-panel">
      <span class="hint" style="left:56px">Let me know when you launch</span>
      <span class="hint" style="left:260px">Get a free gift with your first pack</span>
      <div class="email-field">Enter Your Email</div>
      <div class="notify-btn">Notify Me</div>
    </div>
  </header>

  <h2 class="section-title steps-title" id="how">How it works</h2>

  <div class="step" style="left:152px">
    <svg class="icon" width="30" height="28" viewBox="0 0 30 28"><rect x="2" y="6" width="20" height="20" fill="none" stroke="#fff" stroke-width="2.2"/><path d="M7 15l6 6L28 2" fill="none" stroke="#fff" stroke-width="3"/></svg>
    <h3>Choose a plan</h3>
    <p>There will be plans for all budgets and styles.</p>
    <div class="step-num">1</div>
  </div>
  <div class="step" style="left:293px">
    <svg class="icon" width="30" height="30" viewBox="0 0 30 30"><circle cx="13" cy="9" r="7" fill="none" stroke="#fff" stroke-width="1.6"/><path d="M11 9v13l-3-3-2 2 6 7h10l2-10-9-2V9z" fill="none" stroke="#fff" stroke-width="1.8" stroke-linejoin="round"/></svg>
    <h3>Choose how often</h3>
    <p>Decide whether you would like to receive new packages every 3 or 6 months.</p>
    <div class="step-num">2</div>
  </div>
  <div class="step" style="left:432px">
    <svg class="icon" width="30" height="28" viewBox="0 0 30 28"><rect x="9" y="2" width="17" height="12" fill="none" stroke="#fff" stroke-width="1.8"/><path d="M9 6l8.5 5L26 6" fill="none" stroke="#fff" stroke-width="1.5"/><path d="M2 20h8l6 3 10-5-2 6-10 3H2z" fill="#fff"/></svg>
    <h3>Get your pack</h3>
    <p>We'll send out your first pack right away and then again every 3 or 6 months.</p>
    <div class="step-num">3</div>
  </div>

  <section class="abs plans" id="plans"></section>
  <h2 class="section-title plans-title">Plan</h2>

  <div class="plan-card" style="left:154px">
    <div class="plan-tab" style="left:0">Comfort</div>
    <div class="photo" role="img" aria-label="Black and white photo of three men in underwear" style="left:12px;top:26px;width:106px;height:66px;background:linear-gradient(135deg,#9a9a9a,#dcdcdc 50%,#7a7a7a)"></div>
    <div class="photo" role="img" aria-label="Product photo of grey boxer briefs" style="left:125px;top:26px;width:58px;height:32px;background:linear-gradient(135deg,#cfcfcf,#8c8e96)"></div>
    <div class="photo" role="img" aria-label="Product photo of striped grey socks" style="left:125px;top:64px;width:58px;height:34px;background:linear-gradient(135deg,#b8b8b8,#6f7078)"></div>
    <div class="price" style="left:101px">$ 40</div>
    <div class="buy" style="left:138px">Get it !</div>
  </div>
  <div class="plan-card" style="left:362px">
    <div class="plan-tab" style="left:158px">Style</div>
    <div class="photo" role="img" aria-label="Product photo of patterned socks" style="left:19px;top:26px;width:42px;height:40px;background:linear-gradient(135deg,#d9d9d9,#777)"></div>
    <div class="photo" role="img" aria-label="Photo of legs wearing bright striped socks" style="left:83px;top:26px;width:105px;height:66px;background:linear-gradient(135deg,#3b3a6a,#b07a3e 55%,#8a3a2e)"></div>
    <div class="photo" role="img" aria-label="Product photo of purple trunks" style="left:19px;top:72px;width:42px;height:34px;background:linear-gradient(135deg,#6b4a8a,#ccc)"></div>
    <div class="price" style="left:19px">$ 45</div>
    <div class="buy" style="left:56px">Get it !</div>
  </div>

  <div class="perks">
    <div class="perk" style="left:6px">
      <svg width="92" height="26" viewBox="0 0 92 26"><path d="M0 0h76l6 13-6 13H0z" fill="#23252e"/><rect x="6" y="9" width="9" height="7" fill="#fff"/><path d="M15 11h3l2 3v2h-5z" fill="#fff"/><circle cx="86" cy="13" r="6" fill="#23252e"/><path d="M83 13l2 2 4-4" fill="none" stroke="#fff" stroke-width="1.5"/></svg>
      <span>Free Shipping</span>
    </div>
    <div class="perk" style="left:109px">
      <svg width="92" height="26" viewBox="0 0 92 26"><path d="M0 0h76l6 13-6 13H0z" fill="#23252e"/><rect x="7" y="9" width="11" height="8" fill="none" stroke="#fff" stroke-width="1.4"/><path d="M7 9l5.5 4L18 9" fill="none" stroke="#fff" stroke-width="1.1"/><circle cx="86" cy="13" r="6" fill="#23252e"/><path d="M83 13l2 2 4-4" fill="none" stroke="#fff" stroke-width="1.5"/></svg>
      <span>Easy Returns</span>
    </div>
    <div class="perk" style="left:212px">
      <svg width="92" height="26" viewBox="0 0 92 26"><path d="M0 0h76l6 13-6 13H0z" fill="#23252e"/><circle cx="12" cy="13" r="5" fill="none" stroke="#fff" stroke-width="1.4"/><path d="M9 10l6 6M15 10l-6 6" stroke="#fff" stroke-width="1.3"/><circle cx="86" cy="13" r="6" fill="#23252e"/><path d="M83 13l2 2 4-4" fill="none" stroke="#fff" stroke-width="1.5"/></svg>
      <span>Cancel Whenever</span>
    </div>
    <div class="perk" style="left:315px">
      <svg width="92" height="26" viewBox="0 0 92 26"><path d="M0 0h76l6 13-6 13H0z" fill="#23252e"/><circle cx="12" cy="13" r="6" fill="#fff"/><path d="M9 13l2 2 4-4" fill="none" stroke="#23252e" stroke-width="1.5"/><circle cx="86" cy="13" r="6" fill="#23252e"/><path d="M83 13l2 2 4-4" fill="none" stroke="#fff" stroke-width="1.5"/></svg>
      <span>Satisfaction Guaranteed</span>
    </div>
  </div>

  <section class="abs faq" id="faq"></section>
  <h2 class="section-title faq-title">FAQ</h2>

  <div class="faq-card" style="left:152px;top:761px">
    <h3>What is Tidewren Co?</h3>
    <p>Tidewren Co is an Australian subscription service for men's underwear and socks. We stock all your favourite brands and have a range of plans for all budgets and styles.</p>
  </div>
  <div class="faq-card" style="left:293px;top:761px">
    <h3>What is your<br>Satisfaction Guarantee</h3>
    <p>We consider Tidewren Co to be a premium service and customer service is key to that. If for any reason you aren't satisfied simply return your package for a full refund of the charge. In the case of a recurring package we'll refund the most recent charge.</p>
  </div>
  <div class="faq-card" style="left:432px;top:761px">
    <h3>What Is Tidewren Co?</h3>
    <p>Shipping is free Australia wide. We ship all of our packages within 48 hours of payment Monday - Friday. All our packs are shipped through National Parcel with tracking.</p>
  </div>
  <div class="faq-card" style="left:152px;top:874px">
    <h3>What do I get with my<br>Tidewren Plan?</h3>
    <p>You'll get 3 pairs of underwear and 3 pairs of socks. You select the frequency of deliveries when you sign up.</p>
  </div>
  <div class="faq-card" style="left:293px;top:874px">
    <h3>Return Policy</h3>
    <p>We have a 14 day return policy. To be eligible for a return, your item must be unused and in the same condition that you received it. If you need to make a return simply email hello@tidewrenco.com.au</p>
  </div>
  <div class="faq-card" style="left:432px;top:874px">
    <h3>What Brands do you<br>Stock?</h3>
    <p>Tidewren Co currently stocks Northbank, Keelson, Harlow Grey, Ferro &amp; Finch and Quiet Antler. Is your favourite brand missing? Let us know hello@tidewrenco.com.au</p>
  </div>
  <div class="dot" style="left:329px"></div>
  <div class="dot is-active" style="left:346px"></div>
  <div class="dot" style="left:363px;transform:rotate(45deg);width:8px;height:8px;top:990px"></div>
  <div class="dot" style="left:380px"></div>

  <section class="abs about" id="about">
    <h2>About us</h2>
    <h3>We've Got <em>Plans</em> for Every <em>Man</em></h3>
    <p class="lead">We'll be customising plans for every budget and style. Sign up we'll make it easy to keep your bare essentials fresh.</p>
    <p class="body">Sed placerat risus velit, at mollis turpis vulputate et. Suspendisse potenti. Vivamus nec justo enim. Proin dolor enim, venenatis non massa varius, molestie congue urna. Integer mattis dapibus facilisis. Phasellus porta accumsan nunc et mattis. Fusce eu neque mauris. In laoreet quis purus aliquet luctus. Maecenas et varius sapien, finibus gravida tortor. In bibendum gravida augue.</p>
  </section>

  <footer class="abs footer">
    <span class="copy">© Tidewren Co 2014</span>
    <span class="connect">Connect with us</span>
    <span class="social" style="left:424px"></span>
    <span class="social" style="left:441px"></span>
    <span class="social" style="left:458px"></span>
  </footer>

</div>
</body>
</html>
```